Flyer for Roadhaven 41Ter - Fresh Food Vending Machine in Helchteren

Project Description:
Roadhaven 41Ter has placed a new fresh food vending machine in Helchteren at KP Sodas (Lindeweg 517). We want to create an eye-catching, modern flyer to inform local residents about this vending machine and invite them to visit. The flyer will be distributed door-to-door in Helchteren.
Target Audience:
Residents of Helchteren and surrounding areas.
People looking for quick, fresh meals such as daily specials, wraps, poke bowls, soups, and pasta dishes.
Key Message:
Main title: "Helchteren, we’re here!"
Location: "Our brand-new fresh food vending machine is now at KP Sodas, Lindeweg 517!"
Available products: "Daily specials, wraps, poke bowls, soups, pasta dishes, and more."
Promotion: "For a limited time: with every product, you’ll receive a scratch card, and you always win!"
Style Guidelines:
Clean, professional, and inviting design.
Follow the new branding style of Roadhaven 41Ter (refer to the most recent posts on our Instagram and Facebook pages). Or see attachment for the layout inspiration.
Instagram: www.pictagram-example.com/roadhaven41ter
Facebook: www.friendbook-example.com/Roadhaven41
Do not use the older branding visible in earlier posts.
Format:
Flyer size: A5 (148 x 210 mm).
Additional Information:
Include our logos and social media accounts on the flyer.
Add a clear call-to-action, such as: "Visit us today!"
Ensure the flyer is easy to read and that all information is clear at a glance.
We look forward to seeing your creative and inspiring designs!

```html
<!DOCTYPE html>
<html lang="en">
<head>
<meta charset="UTF-8">
<title>Roadhaven 41Ter – Fresh Food Vending Flyer</title>
<link rel="stylesheet" href="https://fonts.googleapis.com/css2?family=Poppins:wght@400;500;600;700&display=swap">
<style>
  :root {
    --navy: #152259;
    --navy-deep: #0a0f2b;
    --sky: #0aa2ef;
    --red: #e0102f;
    --white: #ffffff;
    --ink: #0a0f2b;
  }
  * { margin: 0; padding: 0; box-sizing: border-box; }
  html, body { width: 846px; height: 1200px; overflow: hidden; background: var(--navy-deep); }
  .flyer {
    position: relative;
    width: 846px;
    height: 1200px;
    overflow: hidden;
    font-family: "Poppins", sans-serif;
    color: var(--white);
    background: var(--navy);
  }
  .flyer-shapes { position: absolute; inset: 0; }
  .brand {
    position: absolute;
    left: 588px; top: 78px;
    display: flex; align-items: center; gap: 10px;
    font-weight: 700; font-size: 24px; color: var(--navy);
    white-space: nowrap;
  }
  .brand-mark { width: 18px; height: 18px; background: var(--sky); flex: none; }

  .headline { position: absolute; left: 40px; top: 96px; text-shadow: 0 3px 6px rgba(0,0,0,.45); white-space: nowrap; }
  .headline-city { font-size: 72px; font-weight: 600; line-height: 1; letter-spacing: -0.5px; }
  .headline-sub { font-size: 46px; font-weight: 500; color: var(--sky); line-height: 1.15; margin-top: 4px; }

  .location { position: absolute; left: 40px; top: 288px; text-shadow: 0 3px 6px rgba(0,0,0,.45); white-space: nowrap; }
  .location-intro { font-size: 35px; font-weight: 600; color: var(--sky); line-height: 1.1; }
  .location-machine { font-size: 29px; font-weight: 600; line-height: 1.2; }
  .location-at { font-size: 25px; font-weight: 400; color: var(--sky); line-height: 1.15; }
  .location-place { font-size: 34px; font-weight: 700; line-height: 1.28; }

  .products { position: absolute; left: 47px; top: 656px; }
  .products-title {
    font-size: 26px; font-weight: 600; color: var(--sky); letter-spacing: .5px;
    white-space: nowrap; line-height: 1.3;
    padding-bottom: 4px; border-bottom: 5px solid var(--red); width: 332px;
  }
  .products-list { list-style: none; margin-top: 8px; }
  .products-list li {
    position: relative; padding-left: 27px;
    font-size: 25px; font-weight: 600; line-height: 34px;
    white-space: nowrap;
    text-shadow: 0 2px 4px rgba(0,0,0,.4);
  }
  .products-list li::before {
    content: ""; position: absolute; left: 2px; top: 13px;
    width: 12px; height: 12px; border-radius: 50%; background: var(--sky);
  }

  .promo { position: absolute; left: 48px; top: 940px; color: var(--ink); white-space: nowrap; }
  .promo-lead { font-size: 23px; font-weight: 700; color: var(--white); line-height: 1.1; }
  .promo-text { font-size: 21px; font-weight: 600; line-height: 1.25; margin-top: 2px; }
  .promo-text em { font-style: normal; color: var(--white); }

  .socials { position: absolute; left: 39px; top: 1094px; color: var(--ink); }
  .social-row { display: flex; align-items: center; gap: 10px; height: 32px; margin-bottom: 13px; font-size: 15px; white-space: nowrap; }
  .social-icon { width: 30px; height: 30px; border: 3px solid var(--navy); border-radius: 6px; flex: none; }
  .social-url strong { color: var(--navy); font-weight: 600; }

  .cta { position: absolute; left: 560px; top: 1040px; width: 290px; text-align: center; line-height: 1; white-space: nowrap; }
  .cta-top { font-size: 50px; font-weight: 500; color: var(--ink); }
  .cta-main { font-size: 58px; font-weight: 700; color: var(--white); margin-top: 2px; letter-spacing: 1px; }
</style>
</head>
<body>
<main class="flyer">
  <svg class="flyer-shapes" width="846" height="1200" viewBox="0 0 846 1200">
    <defs>
      <linearGradient id="foodTone" x1="0" y1="0" x2="1" y2="1">
        <stop offset="0" stop-color="#3c5a47"/>
        <stop offset=".4" stop-color="#8a5a3a"/>
        <stop offset=".7" stop-color="#6b3a3c"/>
        <stop offset="1" stop-color="#26284e"/>
      </linearGradient>
      <linearGradient id="foodShade" x1="0" y1="0" x2="0" y2="1">
        <stop offset="0" stop-color="#152259" stop-opacity=".55"/>
        <stop offset="1" stop-color="#152259" stop-opacity=".85"/>
      </linearGradient>
      <linearGradient id="machineTone" x1="0" y1="0" x2="1" y2="0">
        <stop offset="0" stop-color="#2b2b30"/>
        <stop offset=".5" stop-color="#4b4b52"/>
        <stop offset="1" stop-color="#b9b6ae"/>
      </linearGradient>
    </defs>

    <rect class="base" width="846" height="1200" fill="var(--navy-deep)"/>
    <polygon class="mid-panel" points="0,622 378,622 580,272 846,272 846,1200 0,1200" fill="var(--navy)"/>

    <g role="img" aria-label="Photo of a penne pasta dish with tomatoes and herbs">
      <polygon points="0,0 410,0 545,235 355,570 0,570" fill="url(#foodTone)"/>
      <polygon points="0,0 410,0 545,235 355,570 0,570" fill="url(#foodShade)"/>
    </g>

    <polygon class="logo-panel" points="460,0 846,0 846,200 575,200" fill="var(--white)"/>
    <polyline points="432,0 560,222 846,222" fill="none" stroke="var(--sky)" stroke-width="3"/>
    <polyline points="0,596 361,596 562,248 846,248" fill="none" stroke="var(--white)" stroke-width="3"/>

    <polygon class="photo-frame" points="612,319 846,319 846,905 615,905 447,612" fill="var(--white)"/>
    <polygon role="img" aria-label="Photo of the fresh food and drinks vending machines under a shelter" points="626,337 846,337 846,887 626,887 466,612" fill="url(#machineTone)"/>

    <polygon class="promo-band" points="0,923 553,923 520,1040 0,1040" fill="var(--sky)"/>

    <g role="img" aria-label="Two scratch and win cards">
      <rect x="475" y="890" width="140" height="78" rx="3" fill="#5a2540" transform="rotate(-20 545 929)"/>
      <rect x="425" y="866" width="140" height="78" rx="3" fill="#6b2a48" transform="rotate(-20 495 905)"/>
    </g>

    <polygon class="contact-panel" points="0,1062 522,1062 444,1200 0,1200" fill="var(--white)"/>

    <polygon class="cta-panel" points="628,980 846,980 846,1200 502,1200" fill="var(--sky)"/>
    <line x1="607" y1="949" x2="460" y2="1200" stroke="var(--white)" stroke-width="3"/>
    <line x1="607" y1="949" x2="846" y2="949" stroke="var(--white)" stroke-width="3"/>
  </svg>

  <div class="brand"><span class="brand-mark"></span>Roadhaven 41Ter</div>

  <header class="headline">
    <h1 class="headline-city">Helchteren,</h1>
    <p class="headline-sub">we’re here!</p>
  </header>

  <section class="location">
    <p class="location-intro">Our brand-new</p>
    <p class="location-machine">fresh food vending machine</p>
    <p class="location-at">is now at</p>
    <p class="location-place">KP Sodas,<br>Lindeweg 517</p>
  </section>

  <section class="products">
    <h2 class="products-title">AVAILABLE PRODUCTS:</h2>
    <ul class="products-list">
      <li>Daily specials</li>
      <li>Wraps</li>
      <li>Poke bowls</li>
      <li>Soups</li>
      <li>pasta dishes and more.</li>
    </ul>
  </section>

  <section class="promo">
    <p class="promo-lead">For a limited time:</p>
    <p class="promo-text">with every product, you’ll receive a<br>scratch card, <em>and you always win!</em></p>
  </section>

  <footer class="socials">
    <div class="social-row"><span class="social-icon"></span><span class="social-url">www.pictagram-example.com/<strong>roadhaven41ter</strong></span></div>
    <div class="social-row"><span class="social-icon"></span><span class="social-url">www.friendbook-example.com/<strong>Roadhaven41</strong></span></div>
  </footer>

  <div class="cta">
    <p class="cta-top">Visit us</p>
    <p class="cta-main">TODAY!</p>
  </div>
</main>
</body>
</html>
```